Hello,
Marisol Trent Equestrian needs a business card. We are a high performance show jumping stables based at Oakhollow Paddocks in morningotn. We pride ourselves on producing high quality show jumping horses and competing our stock at a high level. My business card need to have my logo on it, and i would like it to have a classic design with a modern touch. I would like it to have quite a natural feel about it. It needs to be in a font which is easy to read as I spend a lot of time competing internationally and overseas, and i need to be able to give it out to breeders and contacts where English isnt their first language. I will need it to include the following details:
-Marisol Trent Equestrian
-Based at Oakhollow Paddocks Mornington
-Address: 17 Pemberly Lane Mornington Victoria 3931
-Mobile number: 0412659048
- website: www.marisoltrentequestrian-example.com
Target Market(s)
For business adults who english may not be their first language
Industry/Entity Type
Business

```html
<!DOCTYPE html>
<html lang="en">
<head>
<meta charset="utf-8">
<title>Marisol Trent Equestrian – Business Card</title>
<link rel="stylesheet" href="https://fonts.googleapis.com/css2?family=Cinzel:wght@400&family=Montserrat:wght@400;500&display=swap">
<style>
  :root {
    --board: #151516;
    --card: #050505;
    --silver: #b9bbbd;
    --silver-soft: #9fa1a3;
    --label: #c4c4c4;
    --glow: rgba(120, 190, 210, 0.45);
  }
  html, body {
    margin: 0;
    padding: 0;
    overflow: hidden;
  }
  .board {
    position: relative;
    width: 1200px;
    height: 1000px;
    background: var(--board);
    overflow: hidden;
  }
  .side-label {
    position: absolute;
    margin: 0;
    font-family: "Cinzel", serif;
    font-weight: 400;
    font-size: 50px;
    letter-spacing: 2px;
    color: var(--label);
    line-height: 1;
  }
  .side-label--front { left: 753px; top: 235px; }
  .side-label--back  { left: 254px; top: 695px; }

  .card {
    position: absolute;
    width: 542px;
    height: 308px;
    background: var(--card);
    box-shadow: 0 0 14px 3px var(--glow);
  }
  .card--front { left: 133px; top: 110px; }
  .card--back  { left: 518px; top: 555px; }

  .card__mark {
    position: absolute;
    left: 24px;
    top: 30px;
    width: 22px;
    height: 22px;
    border-radius: 50%;
    background: var(--silver);
  }
  .card__rule {
    position: absolute;
    left: 22px;
    right: 0;
    top: 50px;
    height: 1px;
    background: var(--silver-soft);
  }
  .card__name {
    position: absolute;
    right: 30px;
    top: 31px;
    margin: 0;
    font-family: "Cinzel", serif;
    font-size: 16px;
    letter-spacing: 0.3px;
    color: var(--silver);
    white-space: nowrap;
  }
  .card__location {
    position: absolute;
    right: 30px;
    top: 55px;
    margin: 0;
    font-family: "Montserrat", sans-serif;
    font-size: 8.5px;
    letter-spacing: 0.4px;
    color: var(--silver-soft);
  }
  .card__contact {
    position: absolute;
    left: 22px;
    top: 240px;
    margin: 0;
    font-family: "Montserrat", sans-serif;
    font-style: normal;
    font-size: 11px;
    letter-spacing: 0.6px;
    line-height: 18px;
    color: var(--silver);
  }
  .card__phone { font-weight: 500; font-size: 11.5px; }

  .card__frame {
    position: absolute;
    left: 0;
    top: 0;
  }
  .card__emblem {
    position: absolute;
    left: 231px;
    top: 100px;
    width: 80px;
    height: 80px;
    border-radius: 50%;
    background: var(--silver);
  }
  .card__name--centered {
    right: auto;
    left: 0;
    width: 100%;
    top: 204px;
    text-align: center;
    font-size: 15px;
  }
</style>
</head>
<body>
<main class="board">

  <h2 class="side-label side-label--front">FRONT</h2>
  <h2 class="side-label side-label--back">BACK</h2>

  <section class="card card--front" aria-label="Business card front">
    <span class="card__mark" aria-hidden="true"></span>
    <div class="card__rule"></div>
    <h1 class="card__name">Marisol Trent Equestrian</h1>
    <p class="card__location">Oakhollow Paddocks Mornington</p>
    <address class="card__contact">
      <span class="card__phone">Ph: 0412659048</span><br>
      17 Pemberly Lane Mornington Victoria 3931<br>
      www.marisoltrentequestrian-example.com
    </address>
  </section>

  <section class="card card--back" aria-label="Business card back">
    <svg class="card__frame" width="542" height="308" viewBox="0 0 542 308" aria-hidden="true">
      <rect x="27.5" y="28.5" width="487" height="254" fill="none" stroke="#b9bbbd" stroke-width="1.5"/>
      <rect x="31.5" y="32.5" width="479" height="246" fill="none" stroke="#b9bbbd" stroke-width="0.6"/>
      <polygon points="33,34 59,34 33,60" fill="#b9bbbd"/>
      <polygon points="509,34 483,34 509,60" fill="#b9bbbd"/>
      <polygon points="33,277 59,277 33,251" fill="#b9bbbd"/>
      <polygon points="509,277 483,277 509,251" fill="#b9bbbd"/>
    </svg>
    <span class="card__emblem" aria-hidden="true"></span>
    <p class="card__name card__name--centered">Marisol Trent Equestrian</p>
  </section>

</main>
</body>
</html>
```